Business Card Design Project

I need a business card design for an Organic drive thru coffee kiosk. We will serve organic coffee, teas & smoothies and will serve healthy breakfast food/snacks for people on the go.
I want the card to have 2-3 colors max (earthy colors like browns, greens and so on).
I have attached the logo I want used and would love to play off the theme of "balance."
Include:
Fair-Leaf Coffee
address: 3170 Morrow Ct. Raleigh, NC 27493
phone: 919-371-4402
website: www.fair-leaf.com (website is not up yet but still include it on card)
email: Joanne@fair-leaf.com
I want one of the following sayings somewhere on the card (the front or back is fine):
"Eat & Drink Well, on the run!"
"Break the fast with Fair-Leaf"
Maybe on the back list what we offer:
-Organic coffee, espresso & tea
-Quorblend smoothies & protein shakes
-Zippy Press (100% fresh local fruit and veggies)
-Healthy Bites
Target Market(s)
College age to 55
Industry/Entity Type
Business
Look and feel
Each slider illustrates characteristics of the customer's brand and the style your logo design should communicate.

```html
<!DOCTYPE html>
<html lang="en">
<head>
<meta charset="utf-8">
<title>Fair-Leaf Coffee — Business Card</title>
<link rel="stylesheet" href="https://fonts.googleapis.com/css2?family=Arimo:wght@400;700&family=Lobster+Two:ital,wght@1,700&display=swap">
<style>
  :root {
    --stage: #3a3a3a;
    --cream: #e9d49c;
    --plum: #5a1f38;
    --plum-ink: #4d1a30;
    --white: #ffffff;
    --latte-light: #b08a68;
    --latte-mid: #8c6a4f;
    --latte-dark: #6e4f3b;
    --swirl: #e6c98e;
    --list-ink: #3e2419;
  }
  * { margin: 0; padding: 0; box-sizing: border-box; }
  html, body {
    width: 1200px;
    height: 848px;
    overflow: hidden;
    background: var(--stage);
    font-family: "Arimo", Arial, sans-serif;
  }
  .card {
    position: absolute;
    width: 300px;
    height: 530px;
    overflow: hidden;
  }

  /* Front */
  .card--front { left: 255px; top: 100px; background: var(--plum); }
  .brand-panel {
    height: 231px;
    background: var(--cream);
    display: flex;
    flex-direction: column;
    align-items: center;
    padding-top: 48px;
  }
  .brand-dot {
    width: 64px;
    height: 64px;
    border-radius: 50%;
    background: var(--plum);
  }
  .brand-name {
    margin-top: 16px;
    font-size: 38px;
    font-weight: 700;
    color: var(--plum);
    letter-spacing: 0.5px;
    line-height: 1;
  }
  .brand-tagline {
    margin-top: 8px;
    font-size: 9.5px;
    font-weight: 700;
    letter-spacing: 2px;
    color: var(--plum);
  }
  .contact {
    color: var(--white);
    text-align: right;
    padding: 0 26px;
  }
  .contact__web {
    margin-top: 136px;
    font-size: 17px;
    font-weight: 700;
    text-align: center;
  }
  .contact__details {
    margin-top: 22px;
    font-size: 13.5px;
    line-height: 1.45;
  }

  /* Back */
  .card--back { left: 645px; top: 218px; }
  .back-art {
    position: absolute;
    inset: 0;
    width: 100%;
    height: 100%;
  }
  .slogan {
    position: absolute;
    top: 66px;
    left: 0;
    right: 0;
    text-align: center;
    font-family: "Lobster Two", "Georgia", cursive;
    font-style: italic;
    font-weight: 700;
    color: var(--plum-ink);
    line-height: 1.25;
  }
  .slogan__lead { font-size: 27px; }
  .slogan__with { font-size: 21px; }
  .slogan__name { display: block; margin-top: 10px; font-size: 36px; }
  .offer-list {
    position: absolute;
    top: 318px;
    left: 22px;
    right: 18px;
    list-style: none;
    color: var(--list-ink);
    font-size: 15.5px;
    line-height: 1.42;
  }
  .offer-list li { padding-left: 12px; position: relative; }
  .offer-list li::before {
    content: "";
    position: absolute;
    left: 0;
    top: 9px;
    width: 6px;
    height: 6px;
    border-radius: 50%;
    background: var(--list-ink);
  }
  .offer-list .offer-note { display: block; font-size: 10.5px; }
</style>
</head>
<body>
  <section class="card card--front" aria-label="Business card front">
    <div class="brand-panel">
      <span class="brand-dot" aria-hidden="true"></span>
      <span class="brand-name">Fair-Leaf</span>
      <span class="brand-tagline">ORGANIC COFFEE + CAFE</span>
    </div>
    <div class="contact">
      <p class="contact__web">www.fair-leaf.com</p>
      <p class="contact__details">
        a: 3170 Morrow Ct. Raleigh,<br>
        NC 27493<br>
        t: 919-371-4402<br>
        e: Joanne@fair-leaf.com
      </p>
    </div>
  </section>

  <section class="card card--back" aria-label="Business card back">
    <svg class="back-art" viewBox="0 0 300 530" preserveAspectRatio="none" role="img" aria-label="Large soft swirl decoration in warm coffee browns">
      <defs>
        <radialGradient id="latteGlow" cx="0.6" cy="0.5" r="0.75">
          <stop offset="0" stop-color="#c9a57a"/>
          <stop offset="0.45" stop-color="#a47d5c"/>
          <stop offset="1" stop-color="#6e4f3b"/>
        </radialGradient>
      </defs>
      <rect width="300" height="530" fill="url(#latteGlow)"/>
    </svg>
    <h2 class="slogan">
      <span class="slogan__lead">Break the fast</span><br>
      <span class="slogan__with">with</span>
      <span class="slogan__name">Fair-Leaf</span>
    </h2>
    <ul class="offer-list">
      <li>Organic coffee,<br>espresso &amp; tea</li>
      <li>Quorblend smoothies &amp;<br>protein shakes</li>
      <li>Zippy Press<span class="offer-note">(100% fresh local fruit and veggies)</span></li>
      <li>Healthy Bites</li>
    </ul>
  </section>
</body>
</html>
```